Snack package design "Driftwood Curled Crisp"

Looking to create a fun package design of snack. Snack is sweet and crunchy; great for people that wants to munch on stuff. Name of the Snack is "Driftwood Curled Crisp". The net weight should be 16oz (453 grams). I added brand "TMvR" Too Mellow Vast Rays on the file. I also added picture of the snack. Package will be a pouch type.

Target Market(s)

People that like sweet snacks

Industry/Entity Type

Food snacks

Requirements
Must have
• Name of Snack "Driftwood Curled Crisp" and logo of company on top left.
Nice to have
• something that's simple and clean design

```html
<!DOCTYPE html>
<html lang="en">
<head>
<meta charset="UTF-8">
<title>Driftwood Curled Crisp – Pouch Front</title>
<link rel="stylesheet" href="https://fonts.googleapis.com/css2?family=Luckiest+Guy&family=Open+Sans:ital,wght@0,600;0,700;1,700&family=Oswald:wght@600&family=Permanent+Marker&display=swap">
<style>
  :root {
    --canvas: #ffffff;
    --pouch-red-dark: #a80e18;
    --pouch-red: #cf1a24;
    --band-red: #e3101c;
    --band-yellow: #f6b800;
    --crisp-light: #e08a3a;
    --crisp-dark: #a8501a;
    --green: #149128;
    --green-dark: #0d6e1e;
    --orange: #ff4a0a;
    --blue: #1192e0;
    --yellow: #f8bf0c;
    --red: #e1101e;
    --white: #ffffff;
    --outline:
      3px 0 0 var(--white), -3px 0 0 var(--white), 0 3px 0 var(--white), 0 -3px 0 var(--white),
      3px 3px 0 var(--white), -3px -3px 0 var(--white), 3px -3px 0 var(--white), -3px 3px 0 var(--white),
      5px 0 0 var(--white), -5px 0 0 var(--white), 0 5px 0 var(--white), 0 -5px 0 var(--white);
  }
  html, body {
    margin: 0;
    width: 1200px;
    height: 958px;
    overflow: hidden;
    background: var(--canvas);
  }
  .canvas { position: relative; width: 1200px; height: 958px; }
  .pouch {
    position: absolute;
    left: 307px;
    top: 49px;
    width: 585px;
    height: 860px;
  }
  .pouch-art { position: absolute; inset: 0; width: 585px; height: 860px; display: block; }

  .fill-bg { fill: url(#pouchBg); }
  .fill-yellow { fill: var(--band-yellow); }
  .fill-red { fill: var(--band-red); }
  .dot { stroke: var(--white); stroke-width: 6; }
  .dot-blue { fill: var(--blue); }
  .dot-green { fill: var(--green); }
  .dot-yellow { fill: var(--yellow); }

  .brand {
    position: absolute;
    left: 70px;
    top: 56px;
    color: var(--white);
    font-family: "Open Sans", sans-serif;
    font-weight: 700;
  }
  .brand-line { font-size: 16px; line-height: 1.2; }
  .brand-name { display: flex; align-items: center; gap: 8px; font-size: 30px; line-height: 1.1; }
  .brand-mark { width: 20px; height: 20px; border-radius: 50%; background: var(--white); }

  .title {
    position: absolute;
    left: 0;
    width: 585px;
    text-align: center;
    text-shadow: var(--outline);
  }
  .title-main {
    top: 168px;
    font-family: "Permanent Marker", cursive;
    font-size: 92px;
    line-height: 1;
    letter-spacing: 1px;
  }
  .c-green { color: var(--green); }
  .c-orange { color: var(--orange); }
  .c-blue { color: var(--blue); }
  .c-yellow { color: var(--yellow); }
  .c-red { color: var(--red); }

  .title-type {
    top: 305px;
    display: flex;
    justify-content: center;
    align-items: flex-end;
    font-family: "Luckiest Guy", cursive;
  }
  .type-big { font-size: 150px; line-height: 0.85; }
  .type-mid { display: flex; flex-direction: column; align-items: center; margin: 0 4px; }
  .type-sub {
    font-family: "Oswald", sans-serif;
    font-weight: 600;
    font-size: 44px;
    line-height: 1;
    color: var(--green);
    margin-bottom: 4px;
  }
  .type-letters { font-size: 92px; line-height: 0.85; letter-spacing: 2px; }

  .tagline-band {
    position: absolute;
    left: 0;
    top: 780px;
    width: 472px;
    height: 60px;
    background: var(--band-red);
    color: var(--white);
    font-family: "Open Sans", sans-serif;
    font-weight: 600;
    font-size: 17px;
    line-height: 25px;
    padding: 6px 0 0 16px;
    box-sizing: border-box;
  }
  .net-weight {
    position: absolute;
    left: 481px;
    top: 747px;
    width: 74px;
    height: 106px;
    background: linear-gradient(135deg, var(--green), var(--green-dark));
    color: var(--white);
    font-family: "Open Sans", sans-serif;
    font-style: italic;
    font-weight: 700;
    text-align: center;
    box-sizing: border-box;
    padding-top: 6px;
  }
  .weight-oz { font-size: 18px; line-height: 22px; }
  .weight-label { font-size: 10px; line-height: 14px; }
  .weight-g { font-size: 22px; line-height: 30px; }
  .weight-rule { position: absolute; left: 481px; top: 855px; width: 74px; height: 5px; background: var(--green); }
</style>
</head>
<body>
<div class="canvas">
  <div class="pouch">
    <svg class="pouch-art" viewBox="0 0 885 1300" xmlns="http://www.w3.org/2000/svg" aria-hidden="false">
      <defs>
        <linearGradient id="pouchBg" x1="0" y1="0" x2="0.4" y2="1">
          <stop offset="0" stop-color="#a80e18"/>
          <stop offset="0.6" stop-color="#cf1a24"/>
          <stop offset="1" stop-color="#a80e18"/>
        </linearGradient>
        <radialGradient id="crispFill" cx="0.5" cy="0.45" r="0.7">
          <stop offset="0" stop-color="#e08a3a"/>
          <stop offset="1" stop-color="#a8501a"/>
        </radialGradient>
      </defs>
      <rect class="fill-bg" width="885" height="1300"/>
      <path class="fill-yellow" d="M0 880 Q330 720 885 730 L885 1300 L0 1300 Z"/>
      <path class="fill-red" d="M0 945 Q360 760 885 752 L885 1300 L0 1300 Z"/>
      <path role="img" aria-label="Photo of golden curled crisp pieces piled together"
            d="M0 1010 Q380 780 885 795 L885 1300 L0 1300 Z" fill="url(#crispFill)"/>

      <circle class="dot dot-blue" cx="445" cy="212" r="30"/>
      <circle class="dot dot-blue" cx="625" cy="200" r="46"/>
      <circle class="dot dot-green" cx="95" cy="500" r="22"/>
      <circle class="dot dot-green" cx="100" cy="610" r="40"/>
      <circle class="dot dot-yellow" cx="815" cy="585" r="40"/>
      <circle class="dot dot-yellow" cx="810" cy="700" r="27"/>
    </svg>

    <div class="brand">
      <div class="brand-line">Too Mellow Vast Rays</div>
      <div class="brand-name"><span class="brand-mark"></span>TMvR</div>
    </div>

    <div class="title title-main"><span class="c-green">Dri</span><span class="c-orange">ft</span><span class="c-blue">wood</span></div>

    <div class="title title-type">
      <span class="type-big c-red">C</span>
      <span class="type-mid">
        <span class="type-sub">CURLED</span>
        <span class="type-letters"><span class="c-orange">R</span><span class="c-blue">I</span><span class="c-yellow">S</span></span>
      </span>
      <span class="type-big c-green">P</span>
    </div>

    <div class="tagline-band">GREAT FOR PEOPLE THAT WANTS TO<br>MUNCH ON STUFF</div>

    <div class="net-weight">
      <div class="weight-oz">16OZ</div>
      <div class="weight-label">NET</div>
      <div class="weight-label">WEIGHT</div>
      <div class="weight-g">453g</div>
    </div>
    <div class="weight-rule"></div>
  </div>
</div>
</body>
</html>
```